Business Card - high end, modern health care

Hey designers!

We need a double sided business card for the boutique, cutting edge physical therapy rehabilitation centre in Sydney's Northern Beaches.

With the most qualified physios in the area The Harbourline Motion Clinic does what other physiotherapy practices do not, we take our time with our patients giving them longer appointments, better physios and therefor faster results!

We guarantee that the service people receive at THMC will be unparalleled.

Hence we need a business card to reflect our modern, boutique, high end service. The final design needs to reflect that we are in a class of our own yet with the feel of beachside retreat.

Below I have attached our logo in both blue on white and white on blue. The exact colour is;
and the font that we have used in our logo is Tex Gyre Aventador.

I like the idea of the blue as the main colour as it is more eye catching and our signage onto the main road will be in this blue and in the interest of consistency across marketing the blue needs to be a part of the design. However I would appreciate a few designs onto a wooden background as this is a visual theme within the fitout of the practice.

The design needs to be of standard size (91x55mm).

Target Market(s)

We target people who have an end outcome in mind and those who have had poor experiences with other providers and ensure that everyone gets the care that they deserve with a premium service that is tailored to the individuals circumstances. As a premium service, the target market is highly educated, business and tech savvy with the additional target market of elderly people who have self funded their retirement and see value in paying for the best ongoing rehabilitation to maintain independence.

Industry/Entity Type

Physical Therapy

Contact Information for Business Card

Name, designation( Titled Musculoskeletal Physiotherapist... there will also be those in the company that have multiple designations ie 5 or 6 words long), phone number, email, facebook, instagram, address

Font styles to use
Sans Serif

Colors

Designer to choose colors to be used in the design.

Requirements
Must have
• Front - The logo as large as possible, blue or wooden theme, and all of the important details.
• Back - A blank space/lines on which to write appointment times (no "Appointment, date, time" etc.)
Nice to have
• facebook url
• logos for facebook and instagram
• Mini logos for the phone and email?

```html
<!DOCTYPE html>
<html lang="en">
<head>
<meta charset="utf-8">
<title>The Harbourline Motion Clinic – Business Card</title>
<link href="https://fonts.googleapis.com/css2?family=Montserrat:wght@400;500;700&display=swap" rel="stylesheet">
<style>
  :root {
    --brand-blue: #0b5cb5;
    --brand-blue-deep: #07489a;
    --wave-blue: #0a3f86;
    --fern-blue: #2a6fc9;
    --paper: #ffffff;
    --rule: #9a9a9a;
    --backdrop: #e6d4a5;
    --ink-light: #ffffff;
  }
  * { box-sizing: border-box; margin: 0; padding: 0; }
  html, body { width: 1200px; height: 1000px; overflow: hidden; }
  body {
    background: var(--backdrop);
    font-family: "Montserrat", sans-serif;
    display: flex;
    flex-direction: column;
    align-items: center;
    justify-content: center;
    gap: 44px;
  }
  .card {
    position: relative;
    width: 700px;
    height: 423px;
    border-radius: 40px;
    overflow: hidden;
    box-shadow: 0 6px 18px rgba(90, 70, 30, 0.18);
  }
  .card--front {
    background: linear-gradient(160deg, var(--brand-blue) 0%, var(--brand-blue-deep) 100%);
    color: var(--ink-light);
  }
  .card--back { background: var(--paper); }

  .motif { position: absolute; right: 0; top: 0; width: 420px; height: 423px; }

  .wordmark { position: absolute; display: flex; align-items: center; gap: 12px; }
  .wordmark__dot { width: 44px; height: 44px; border-radius: 50%; flex: none; }
  .wordmark__name { font-weight: 700; font-size: 27px; line-height: 1; letter-spacing: 0.5px; }
  .wordmark__sub { font-weight: 400; font-size: 17px; letter-spacing: 5px; margin-top: 4px; }

  .card--front .wordmark { left: 52px; top: 98px; color: var(--ink-light); }
  .card--front .wordmark__dot { background: var(--ink-light); }
  .card--back .wordmark { left: 52px; top: 70px; color: var(--brand-blue); }
  .card--back .wordmark__dot { background: var(--brand-blue); }

  .staff { position: absolute; left: 112px; top: 222px; font-size: 13px; line-height: 1.2; letter-spacing: 0.6px; }
  .staff__name { font-weight: 700; font-size: 14px; }
  .contact { position: absolute; left: 118px; top: 290px; display: flex; flex-direction: column; gap: 14px; }
  .contact svg { display: block; }
  .social { display: flex; gap: 6px; margin-left: 6px; }
  .social span { width: 15px; height: 15px; border: 1.6px solid var(--ink-light); border-radius: 3px; }

  .write-lines { position: absolute; left: 52px; right: 52px; top: 140px; }
  .write-lines hr { border: none; border-top: 1.4px solid var(--rule); margin-bottom: 35px; }
</style>
</head>
<body>

  <section class="card card--front" aria-label="Card front">
    <svg class="motif" viewBox="0 0 420 423" role="img" aria-label="Large wave and fern decorative motif">
      <defs>
        <linearGradient id="fernTone" x1="0" y1="0" x2="0" y2="1">
          <stop offset="0" stop-color="#2c72cc"/>
          <stop offset="1" stop-color="#1d5fb6"/>
        </linearGradient>
      </defs>
      <circle cx="240" cy="220" r="200" fill="var(--wave-blue)" opacity="0.75"/>
      <rect x="250" y="0" width="170" height="423" fill="url(#fernTone)" opacity="0.55"/>
    </svg>

    <div class="wordmark">
      <span class="wordmark__dot"></span>
      <div>
        <div class="wordmark__name">THE HARBOURLINE</div>
        <div class="wordmark__sub">MOTION CLINIC</div>
      </div>
    </div>

    <div class="staff">
      <div class="staff__name">Name</div>
      <div>MUSCULOSKELETAL</div>
      <div>PHYSIOTHERAPIST</div>
    </div>

    <div class="contact">
      <svg width="16" height="16" viewBox="0 0 24 24" aria-label="Phone">
        <path fill="#fff" d="M6.6 10.8c1.4 2.8 3.8 5.1 6.6 6.6l2.2-2.2c.3-.3.7-.4 1-.2 1.1.4 2.3.6 3.6.6.6 0 1 .4 1 1V20c0 .6-.4 1-1 1C10.6 21 3 13.4 3 4c0-.6.4-1 1-1h3.5c.6 0 1 .4 1 1 0 1.3.2 2.5.6 3.6.1.3 0 .7-.2 1z"/>
      </svg>
      <svg width="20" height="14" viewBox="0 0 20 14" aria-label="Email">
        <rect x="1" y="1" width="18" height="12" fill="none" stroke="#fff" stroke-width="1.6"/>
        <path d="M1 1l9 7 9-7" fill="none" stroke="#fff" stroke-width="1.6"/>
      </svg>
      <div class="social" aria-label="Social profiles"><span></span><span></span></div>
    </div>
  </section>

  <section class="card card--back" aria-label="Card back">
    <div class="wordmark">
      <span class="wordmark__dot"></span>
      <div>
        <div class="wordmark__name">THE HARBOURLINE</div>
        <div class="wordmark__sub">MOTION CLINIC</div>
      </div>
    </div>
    <div class="write-lines" aria-label="Lines for appointment notes">
      <hr><hr><hr><hr><hr><hr><hr>
    </div>
  </section>

</body>
</html>
```